Private Medical Clinic needs a letterhead design

Letterhead that can be edited. Letter head is needed for printing official doctor's notes, referrals, etc in a medical clinic. The letterhead should use the attached logos

```html
<!DOCTYPE html>
<html lang="en">
<head>
<meta charset="utf-8">
<title>Still Meadow – Letterhead</title>
<link href="https://fonts.googleapis.com/css2?family=Lora:wght@400&family=Lato:wght@400&display=swap" rel="stylesheet">
<style>
  :root {
    --backdrop: #cfc4c1;
    --paper: #ffffff;
    --ink: #3b4137;
    --forest: #424b40;
    --watermark: #f1f1ef;
  }
  * { margin: 0; padding: 0; box-sizing: border-box; }
  html, body {
    width: 1200px;
    height: 784px;
    overflow: hidden;
    background: var(--backdrop);
  }
  .letterhead {
    position: absolute;
    left: 316px;
    top: 22px;
    width: 568px;
    height: 740px;
    background: var(--paper);
    box-shadow: 0 6px 18px rgba(60, 50, 48, 0.18);
    overflow: hidden;
  }
  .brand {
    position: absolute;
    left: 44px;
    top: 48px;
    display: flex;
    align-items: center;
    gap: 10px;
    font-family: "Lora", serif;
    font-weight: 400;
    font-size: 30px;
    color: var(--ink);
    letter-spacing: 0.2px;
  }
  .brand-dot {
    width: 12px;
    height: 12px;
    border-radius: 50%;
    background: var(--ink);
  }
  .contact {
    position: absolute;
    right: 40px;
    top: 46px;
    padding-left: 16px;
    border-left: 1px solid var(--ink);
    font-family: "Lato", sans-serif;
    font-size: 10.5px;
    line-height: 1.45;
    color: var(--ink);
  }
  .contact-row {
    display: flex;
    align-items: center;
    gap: 6px;
  }
  .contact-row svg {
    width: 9px;
    height: 9px;
    flex: none;
  }
  .contact-row.plain { padding-left: 15px; }
  .watermark {
    position: absolute;
    left: 114px;
    top: 220px;
    width: 340px;
    height: 300px;
    border-radius: 50%;
    background: radial-gradient(circle, var(--watermark) 0%, rgba(241,241,239,0.6) 55%, rgba(255,255,255,0) 72%);
  }
  .footer-wave {
    position: absolute;
    left: 0;
    bottom: 0;
    width: 568px;
    height: 170px;
  }
</style>
</head>
<body>
  <main class="letterhead">
    <div class="brand">
      <span class="brand-name">Still Meadow</span>
      <span class="brand-dot"></span>
    </div>

    <address class="contact">
      <div class="contact-row plain">1234 First Line Address</div>
      <div class="contact-row plain">5678 Second Line Address</div>
      <div class="contact-row">
        <svg viewBox="0 0 10 10"><path d="M2 1 L4 1 L4.6 3 L3.4 4 Q4.5 6 6 6.6 L7 5.4 L9 6 L9 8 Q5 9 1.5 5 Q1 3 2 1Z" fill="var(--ink)"/></svg>
        <span>(111) 999-0000</span>
      </div>
      <div class="contact-row">
        <svg viewBox="0 0 10 10"><rect x="0.5" y="2" width="9" height="6" fill="none" stroke="var(--ink)"/><path d="M0.5 2 L5 5.5 L9.5 2" fill="none" stroke="var(--ink)"/></svg>
        <span>info@yourmail.com</span>
      </div>
      <div class="contact-row">
        <svg viewBox="0 0 10 10"><circle cx="5" cy="5" r="4.2" fill="none" stroke="var(--ink)"/><path d="M1 5 H9 M5 0.8 Q2.5 5 5 9.2 M5 0.8 Q7.5 5 5 9.2" fill="none" stroke="var(--ink)" stroke-width="0.7"/></svg>
        <span>www.yourwesite.com</span>
      </div>
    </address>

    <div class="watermark" role="img" aria-label="Faint botanical watermark of a seed head with roots"></div>

    <svg class="footer-wave" viewBox="0 0 568 170" preserveAspectRatio="none" aria-hidden="true">
      <path d="M0 60 Q180 150 568 120 L568 170 L0 170 Z" fill="var(--forest)"/>
      <path d="M0 26 Q190 128 568 106" fill="none" stroke="var(--forest)" stroke-width="5"/>
    </svg>
  </main>
</body>
</html>
```